Plakat für Verein
Zielgruppe
Wir möchten eine Veranstaltung für unseren Verein - Hinterkalmbacher Heimatpflegeverein machen.
Aufgabenstellung
Die Party der Golden 20er
Glanz-Glamour-Lebenslust
Tanzen wie früher - Feiern wie nie
21. März - Uhrzeit: 20.30 im Saal KM
Live mit DJaneMarlies
Dresscode: Goldene 20er - Fransen, Federn, Hosenträger, Zylinder
Farbe: Gold/Schgwarz

```html
<!DOCTYPE html>
<html lang="de">
<head>
<meta charset="utf-8">
<title>Die Party der Golden 20er</title>
<link href="https://fonts.googleapis.com/css2?family=Monoton&family=Poiret+One&family=Montserrat:wght@400;600;700&display=swap" rel="stylesheet">
<style>
  :root {
    --black: #070605;
    --gold-deep: #6b4a1c;
    --gold: #b98a3c;
    --gold-soft: #f0cf8a;
    --cream: #fff3d6;
    --white: #ffffff;
    --grey: #dcd8d0;
  }
  html, body { margin: 0; padding: 0; overflow: hidden; background: var(--black); }
  .poster {
    position: relative;
    width: 848px;
    height: 1200px;
    overflow: hidden;
    background: var(--black);
    color: var(--white);
  }
  .poster__photo {
    position: absolute;
    inset: 0;
    background:
      radial-gradient(ellipse 150px 70px at 40% 8%, rgba(255,255,255,0.16), transparent 100%),
      radial-gradient(ellipse 90px 120px at 2% 62%, rgba(245,245,245,0.85), rgba(220,220,220,0.35) 55%, transparent 100%),
      radial-gradient(ellipse 90px 160px at 100% 78%, rgba(245,240,225,0.8), rgba(220,210,190,0.3) 60%, transparent 100%),
      radial-gradient(ellipse 150px 110px at 43% 57%, rgba(240,200,110,0.95), rgba(190,130,50,0.75) 45%, transparent 100%),
      radial-gradient(circle 40px at 25% 61%, rgba(255,236,180,0.95), transparent 100%),
      radial-gradient(circle 38px at 23% 73%, rgba(255,230,170,0.9), transparent 100%),
      radial-gradient(circle 36px at 32% 76%, rgba(255,232,175,0.85), transparent 100%),
      radial-gradient(circle 34px at 69% 62%, rgba(255,225,160,0.9), transparent 100%),
      radial-gradient(ellipse 260px 200px at 70% 77%, rgba(205,130,95,0.65), rgba(150,90,60,0.35) 55%, transparent 100%),
      radial-gradient(ellipse 360px 320px at 42% 70%, rgba(120,85,40,0.7), transparent 100%),
      linear-gradient(180deg, #050505 0%, #0e0c0a 30%, #2b2118 60%, #251c14 85%, #0d0b09 100%);
  }
  .tagline {
    position: absolute;
    top: 18px; left: 0; width: 100%;
    text-align: center;
    font-family: "Poiret One", sans-serif;
    font-size: 31px;
    margin: 0;
    text-shadow: 0 0 1px var(--white);
  }
  .title {
    position: absolute;
    top: 58px; left: 0; width: 100%;
    margin: 0;
    text-align: center;
    font-family: "Monoton", sans-serif;
    font-weight: 400;
    font-size: 86px;
    line-height: 100px;
    letter-spacing: 0;
    white-space: nowrap;
  }
  .claim {
    position: absolute;
    top: 264px; left: 0; width: 100%;
    text-align: center;
    font-family: "Poiret One", sans-serif;
    font-size: 52px;
    margin: 0;
    text-shadow: 0 0 1px var(--white);
  }
  .artist {
    position: absolute;
    top: 362px; right: 32px;
    font-family: "Poiret One", sans-serif;
    font-size: 40px;
    margin: 0;
    text-shadow: 0 0 1px var(--white), 0 0 1px var(--white), 0.5px 0 0 var(--white);
  }
  .event-info {
    position: absolute;
    left: 38px; top: 1108px;
  }
  .event-info__date {
    margin: 0;
    font-family: "Montserrat", sans-serif;
    font-weight: 700;
    font-size: 26px;
    color: var(--white);
  }
  .event-info__dresscode {
    margin: 3px 0 0;
    font-family: "Montserrat", sans-serif;
    font-weight: 400;
    font-size: 15.5px;
    color: var(--grey);
  }
  .club {
    position: absolute;
    left: 615px; top: 1054px;
    width: 220px;
    text-align: center;
  }
  .club__mark {
    display: block;
    margin: 0 auto 18px;
    width: 58px; height: 58px;
    border-radius: 50%;
    background: var(--white);
  }
  .club__name {
    margin: 0;
    font-family: "Montserrat", sans-serif;
    font-weight: 600;
    font-size: 15px;
    line-height: 21px;
    text-transform: uppercase;
    color: var(--white);
  }
</style>
</head>
<body>
  <main class="poster">
    <div class="poster__photo" role="img" aria-label="Foto: Hand mit rot lackierten Nägeln hält ein Martiniglas mit goldenem, spritzendem Getränk vor goldenen Lichtpunkten"></div>

    <p class="tagline">Tanzen wie früher - Feiern wie nie!</p>
    <h1 class="title">DIE PARTY DER<br>GOLDEN 20ER</h1>
    <p class="claim">Glanz - Glamour - Lebenslust</p>
    <p class="artist">Live mit DJane Marlies</p>

    <div class="event-info">
      <p class="event-info__date">21. MÄRZ - UHRZEIT: 20:30 IM SAAL KM</p>
      <p class="event-info__dresscode">Dresscode: Goldene 20er - Fransen, Federn, Hosenträger, Zylinder</p>
    </div>

    <div class="club">
      <span class="club__mark"></span>
      <p class="club__name">Hinterkalmbacher<br>Heimatpflegeverein</p>
    </div>
  </main>
</body>
</html>
```